Business Card Design for a Sound engineer and DJ

We would like a residn of the business card.

Logo must remain the same.
The card is for the owner of the company.
The business card is in Arabic as the company is based in Kuwait.
The company specializes in sound engineering for singers concerts and events and in addition DJ.
The color options is up to the designer but we would like it masculine as the owner is a man.

Target Market(s)

All ages

Industry/Entity Type

Media

Contact Information for Business Card

Name:
Eng. Tarek Halabi
م/طارق حلبي

The name above is in Arabic and English.

Title: General Manager
Mobile: +965 66307852
Office: +965 22486037
Email: info@sawtarin.net

Address:
Office no. 3
1st floor
Almarfa Complex
Rashed AlQeblawi St.
Salmiya
Kuwait

Instagram: @sawtarin
Snap: sawtarin

Requirements
Nice to have
• can we have Instagram icon and snap icon and a phone vector and email?
• Instead of writing the words

```html
<!DOCTYPE html>
<html lang="en">
<head>
<meta charset="utf-8">
<title>Sawtarin – Business Card</title>
<link rel="stylesheet" href="https://fonts.googleapis.com/css2?family=Open+Sans:wght@400;600&family=Noto+Sans+Arabic:wght@400;600&display=swap">
<style>
  :root {
    --stage: #141414;
    --card-deep: #0b1024;
    --card-mid: #1a2550;
    --glow: #4d6fb8;
    --ink-white: #f2f3f8;
    --accent-purple: #8a3fae;
    --accent-magenta: #b4449e;
    --brand-violet: #a88ce0;
    --paper: #ffffff;
    --address-purple: #7a2e9e;
  }
  * { margin: 0; padding: 0; box-sizing: border-box; }
  html, body { width: 1200px; height: 722px; overflow: hidden; background: var(--stage); }
  body { position: relative; font-family: "Open Sans", "Noto Sans Arabic", sans-serif; }

  .card {
    position: absolute;
    left: 320px;
    width: 560px;
    height: 320px;
    border-radius: 4px;
    box-shadow: 0 4px 14px rgba(0,0,0,.6);
    overflow: hidden;
  }
  .card--front {
    top: 31px;
    background:
      radial-gradient(ellipse 300px 170px at 28% 8%, rgba(77,111,184,.85), rgba(77,111,184,0) 70%),
      linear-gradient(180deg, var(--card-mid) 0%, var(--card-deep) 85%);
  }
  .card--back { top: 371px; background: var(--paper); }

  .brand {
    position: absolute;
    left: 34px;
    top: 150px;
    width: 190px;
    text-align: center;
    color: var(--ink-white);
  }
  .brand__name {
    font-size: 30px;
    font-weight: 600;
    color: var(--brand-violet);
    letter-spacing: 3px;
    line-height: 1;
    margin-bottom: 24px;
  }
  .brand__tagline {
    font-size: 11px;
    font-weight: 600;
    letter-spacing: 1.6px;
    line-height: 1.3;
  }
  .brand__tagline-ar {
    font-family: "Noto Sans Arabic", sans-serif;
    font-size: 13px;
    line-height: 1.3;
  }

  .holder {
    position: absolute;
    right: 35px;
    top: 50px;
    text-align: right;
    color: var(--ink-white);
  }
  .holder__name-ar {
    font-family: "Noto Sans Arabic", sans-serif;
    font-size: 22px;
    color: var(--accent-magenta);
    line-height: 1.2;
  }
  .holder__name-en {
    font-size: 20px;
    color: var(--accent-purple);
    line-height: 1.3;
  }
  .holder__title { font-size: 14px; line-height: 1.6; }

  .contacts {
    margin-top: 30px;
    font-size: 14px;
    line-height: 19px;
  }
  .contacts dt { float: left; clear: left; width: 26px; text-align: left; }
  .contacts dd { text-align: right; }
  .social { margin-top: 9px; font-size: 14px; line-height: 19px; }

  .address {
    position: absolute;
    left: 0; right: 0;
    top: 138px;
    text-align: center;
    color: var(--address-purple);
    font-size: 13.5px;
    line-height: 21px;
  }
  .address__label { font-weight: 600; }
</style>
</head>
<body>
  <section class="card card--front">
    <div class="brand">
      <div class="brand__name">SAWTARIN</div>
      <div class="brand__tagline">DJ - SOUND ENG. - LIGHTING</div>
      <div class="brand__tagline-ar" dir="rtl">دي جي - هندسة صوت - إضاءة</div>
    </div>

    <div class="holder">
      <div class="holder__name-ar" dir="rtl">م/طارق حلبي</div>
      <div class="holder__name-en">Eng. Tarek Halabi</div>
      <div class="holder__title">General Manager</div>

      <dl class="contacts">
        <dt>M:</dt><dd>+965 66307852</dd>
        <dt>P:</dt><dd>+965 22486037</dd>
        <dt>E:</dt><dd>info@sawtarin.net</dd>
      </dl>
      <div class="social">
        <div>Instagram @sawtarin</div>
        <div>Snap sawtarin</div>
      </div>
    </div>
  </section>

  <section class="card card--back">
    <div class="address">
      <div class="address__label">[Our Address]</div>
      <div>Office no. 3, 1st floor, Almarfa Complex, Rashed AlQeblawi St., Salmiya, Kuwait</div>
    </div>
  </section>
</body>
</html>
```